PLUMBING VAN LOGO/VINYL GRAPHIC CONTEST!

Our target audience is builders, contractors, designers, architects.

Upon discussion with some vinyl wrap companies we are now moving away from a full wrap and going for more simplistic lettering and logo design on the truck.
We are looking to apply vinyl graphics on top of a silver color Brannoc hauler 3400. (See attached picture for JUST CUT VINYL style design.

We would like to have our logo incorporated on to the sides of the truck (Must be shrunken down to fit the full logo - no cut off half images)

We would also like to have Custom homes, Additions, Renovations, as well as Commercial/Industrial incorporated onto the side of the van and also the back doors.

We would like to see variations of black and blue on top of the silver for a good color contrast. No light colours for the writing.

Hi Designers,

We are going to be changing the overall design stance of our project, we didn't find anything we particularly liked enough to use as a wrap for our trucks.

We would like to see some more simplistic ideas, and we have decided to keep the silver color of our trucks as a background. We will be going with vinyl graphics on top of the silver backdrop, instead of a full van wrap/color change.

With any new submissions, we would prefer to see our logo and our services listed on the truck, with different ideas for placement. Having a silver van color, we would prefer some darker bolder colors like black, blue, etc. and to avoid any light color schemes.

Important things to have on the design

Kestrow Plumbing Ltd
(logo)
(custom homes, additions, renovations)
(commercial/industrial)

Thank you to everybody who has/will submit designs.

• We are open to different fonts. We like the font in the logo but are open to other ideas.

• Kestrow Plumbing Ltd , Custom Homes, Additions, Renovations, Commercial/Residential
• Silver background on van, kestrow plumbing logo and kestrow plumbing ltd written on

```html
<!DOCTYPE html>
<html lang="en">
<head>
<meta charset="utf-8">
<title>Kestrow Plumbing – Van Side Vinyl Graphics</title>
<link rel="stylesheet" href="https://fonts.googleapis.com/css2?family=Exo:wght@500&family=Montserrat:wght@500;700&display=swap">
<style>
  :root {
    --page: #ffffff;
    --silver: #a9abae;
    --silver-light: #bdbfc2;
    --trim: #3a3b3e;
    --brand-blue: #1666c4;
    --ink: #111214;
    --url-light: #e6e7e9;
  }
  html, body {
    margin: 0;
    width: 1200px;
    height: 1200px;
    overflow: hidden;
    background: var(--page);
  }
  .sheet { display: block; width: 1200px; height: 1200px; }
  .van-body { fill: var(--silver); }
  .van-trim { fill: var(--trim); }
  .accent { fill: var(--brand-blue); }
  .sector-line {
    font-family: "Montserrat", sans-serif;
    font-weight: 500;
    font-size: 17px;
    letter-spacing: 3.5px;
    fill: var(--ink);
  }
  .brand-name {
    font-family: "Exo", sans-serif;
    font-weight: 500;
    fill: var(--brand-blue);
  }
  .brand-name--main { font-size: 100px; }
  .brand-name--sub { font-size: 42px; letter-spacing: 9px; }
  .services {
    font-family: "Montserrat", sans-serif;
    font-weight: 700;
    font-size: 20px;
    fill: var(--ink);
  }
  .phone {
    font-family: "Montserrat", sans-serif;
    font-weight: 700;
    font-size: 21px;
    fill: var(--ink);
  }
  .url {
    font-family: "Montserrat", sans-serif;
    font-weight: 500;
    font-size: 21px;
    letter-spacing: 3px;
    fill: var(--url-light);
  }
  .url--small {
    font-size: 11px;
    letter-spacing: 0;
    fill: var(--brand-blue);
  }
  .social-dot { fill: var(--brand-blue); }
  .bullet { fill: var(--brand-blue); }
  .bullet--light { fill: var(--url-light); }
</style>
</head>
<body>
<svg class="sheet" viewBox="0 0 1200 1200" xmlns="http://www.w3.org/2000/svg">

  <!-- Layout A: blue side stripe -->
  <g class="van van--stripe">
    <g role="img" aria-label="Silver van side, flat">
      <rect class="van-body" x="32" y="108" width="1138" height="392" rx="40"/>
      <rect class="van-trim" x="32" y="412" width="1138" height="76"/>
    </g>

    <text class="sector-line" x="754" y="153" text-anchor="middle">COMMERCIAL / INDUSTRIAL</text>
    <text class="brand-name brand-name--main" x="431" y="262" textLength="667" lengthAdjust="spacingAndGlyphs">KESTROW</text>
    <text class="brand-name brand-name--sub" x="550" y="312" textLength="438" lengthAdjust="spacing">PLUMBING</text>

    <polygon class="accent" points="50,364 1100,338 1096,374 46,396"/>
    <circle class="social-dot" cx="134" cy="380" r="10" fill="#ffffff" style="fill:#ffffff"/>
    <circle class="social-dot" cx="163" cy="380" r="10" style="fill:#ffffff"/>
    <circle class="social-dot" cx="194" cy="380" r="10" style="fill:#ffffff"/>
    <text class="phone" x="228" y="386">253-555-0187</text>
    <text class="services" x="512" y="376" textLength="498" lengthAdjust="spacingAndGlyphs">CUSTOM HOMES  ·  ADDITIONS  ·  RENOVATIONS</text>

    <text class="url" x="310" y="474" textLength="480" lengthAdjust="spacing">www.kestrowplumbing.com</text>

    <polygon class="accent" points="1075,406 1162,275 1162,406"/>
    <polygon class="accent" points="1025,481 1050,438 1162,438 1162,481"/>
  </g>

  <!-- Layout B: compact contact block on cab door -->
  <g class="van van--door">
    <g role="img" aria-label="Silver van side, flat">
      <rect class="van-body" x="32" y="673" width="1138" height="392" rx="40"/>
      <rect class="van-trim" x="32" y="977" width="1138" height="76"/>
    </g>

    <text class="sector-line" x="754" y="720" text-anchor="middle">COMMERCIAL / INDUSTRIAL</text>
    <text class="brand-name brand-name--main" x="431" y="827" textLength="667" lengthAdjust="spacingAndGlyphs">KESTROW</text>
    <text class="brand-name brand-name--sub" x="550" y="877" textLength="438" lengthAdjust="spacing">PLUMBING</text>

    <text class="services" x="512" y="936" textLength="498" lengthAdjust="spacingAndGlyphs">CUSTOM HOMES  ·  ADDITIONS  ·  RENOVATIONS</text>

    <circle class="social-dot" cx="134" cy="935" r="10"/>
    <circle class="social-dot" cx="163" cy="935" r="10"/>
    <circle class="social-dot" cx="194" cy="935" r="10"/>
    <text class="phone" x="225" y="942">(253) 555-0187</text>
    <text class="url url--small" x="227" y="959">www.kestrowplumbing.com</text>

    <polygon class="accent" points="1075,971 1162,840 1162,971"/>
    <polygon class="accent" points="1025,1046 1050,1003 1162,1003 1162,1046"/>
  </g>
</svg>
</body>
</html>
```